Brantley Advisory Group provides support for renewable energy projects to utilities and suppliers

I need a professional looking business card that is both simple and elegant and unique. My clients are mostly large organizations not individuals. I am a consultant with my own company that is small but would like to give clients the impression I am larger. Smart grid, fiber optics, software, field hardware, distribution automation, substation automation, operations, energy storage/batteries, microgrids, customer service, strategy/roadmaps, conservation, Automated Metering Infrastruture (AMI or smart meters) are all areas of focus.

Target Market(s)

Utilities, suppliers, governmental agencies involved in energy. All types of energy especially natural gas and electrical. Especially renewable energy or green projects.

Contact Information for Business Card

Name - Mark Brantley Cell Phone - 425.318.2746 Email - mbrantley@brantleyag-example.com
Company - Brantley Advisory Group (logo) Title - Principal

Font styles to use
Serif
Sans Serif

Colors

Designer to choose colors to be used in the design.

Requirements
Must have
• Simple and professional and powerful.
• Unique/creative design.
Nice to have
• Utilize color scheme to accent logo colors. Maybe some geometric pattern on edge of card with color.
Should not have
• Busy, complicated, traditional

```html
<!DOCTYPE html>
<html lang="en">
<head>
<meta charset="utf-8">
<title>Brantley Advisory Group – Business Card</title>
<link rel="stylesheet" href="https://fonts.googleapis.com/css2?family=Open+Sans:wght@400;600;700&display=swap">
<style>
  :root {
    --backdrop: #e6e7e9;
    --card: #f4f4f3;
    --navy: #233574;
    --green: #4f7d33;
    --text-dark: #2a2f45;
    --text-muted: #3b3f4d;
  }
  * { margin: 0; padding: 0; box-sizing: border-box; }
  html, body {
    width: 1200px;
    height: 923px;
    overflow: hidden;
    background: var(--backdrop);
    font-family: "Open Sans", Arial, sans-serif;
  }
  .stage {
    width: 1200px;
    height: 923px;
    display: flex;
    align-items: center;
    justify-content: center;
  }
  .business-card {
    position: relative;
    width: 840px;
    height: 480px;
    background: var(--card);
    box-shadow: 0 6px 24px rgba(0, 0, 0, 0.12);
    overflow: hidden;
  }
  .color-bands {
    position: absolute;
    inset: 0;
    width: 840px;
    height: 480px;
  }
  .band-navy { fill: var(--navy); }
  .band-green { fill: var(--green); }

  .company-mark {
    position: absolute;
    left: 120px;
    top: 150px;
    display: flex;
    align-items: center;
    gap: 14px;
  }
  .company-square {
    width: 32px;
    height: 32px;
    border: 4px solid var(--green);
  }
  .company-name {
    font-size: 32px;
    font-weight: 700;
    color: var(--navy);
  }

  .person {
    position: absolute;
    right: 72px;
    top: 292px;
    text-align: right;
  }
  .person-name {
    font-size: 22px;
    font-weight: 600;
    color: var(--text-dark);
    line-height: 1.2;
  }
  .person-title {
    font-size: 14px;
    color: var(--text-muted);
    margin-top: 2px;
  }

  .contact-list {
    position: absolute;
    left: 130px;
    top: 292px;
    list-style: none;
  }
  .contact-item {
    display: flex;
    align-items: center;
    gap: 9px;
    font-size: 14px;
    color: var(--text-muted);
    line-height: 1;
    margin-bottom: 8px;
  }
  .contact-icon {
    width: 14px;
    height: 14px;
    flex: none;
  }
  .icon-bg { fill: var(--green); }
  .icon-line { fill: none; stroke: #fff; stroke-width: 1.4; stroke-linecap: round; stroke-linejoin: round; }
</style>
</head>
<body>
<main class="stage">
  <article class="business-card">
    <svg class="color-bands" viewBox="0 0 840 480" aria-hidden="true">
      <polygon class="band-navy" points="0,400 408,400 398,480 0,480"/>
      <polygon class="band-green" points="428,358 840,358 840,480 412,480"/>
    </svg>

    <div class="company-mark">
      <span class="company-square" aria-hidden="true"></span>
      <span class="company-name">Brantley Advisory Group</span>
    </div>

    <div class="person">
      <div class="person-name">Mark Brantley</div>
      <div class="person-title">Principal</div>
    </div>

    <ul class="contact-list">
      <li class="contact-item">
        <svg class="contact-icon" viewBox="0 0 15 15" aria-hidden="true">
          <rect class="icon-bg" width="15" height="15" rx="2"/>
          <rect class="icon-line" x="5" y="2.5" width="5" height="10" rx="1"/>
        </svg>
        <span>425.318.2746</span>
      </li>
      <li class="contact-item">
        <svg class="contact-icon" viewBox="0 0 15 15" aria-hidden="true">
          <rect class="icon-bg" width="15" height="15" rx="2"/>
          <rect class="icon-line" x="3" y="4.5" width="9" height="6"/>
          <polyline class="icon-line" points="3,4.5 7.5,8 12,4.5"/>
        </svg>
        <span>mbrantley@brantleyag-example.com</span>
      </li>
      <li class="contact-item">
        <svg class="contact-icon" viewBox="0 0 15 15" aria-hidden="true">
          <rect class="icon-bg" width="15" height="15" rx="2"/>
          <circle class="icon-line" cx="7.5" cy="7.5" r="4.5"/>
          <line class="icon-line" x1="3" y1="7.5" x2="12" y2="7.5"/>
          <ellipse class="icon-line" cx="7.5" cy="7.5" rx="2" ry="4.5"/>
        </svg>
        <span>www.brantleyag-example.com</span>
      </li>
    </ul>
  </article>
</main>
</body>
</html>
```